依頼概要
本サービスの集客用FAXDMのデザインをお願い致します。

■コンセプト
「冷凍食品専門の物流倉庫!機能充実した最新設備が特長です」
※参考、物流倉庫サービスとは:https://www.kawanami-corp.jp/hokanbox/post-218

■ターゲット像:
★「冷凍食品・冷蔵食材」を扱う企業
・倉庫の確保がしたい物流会社も許容
→メーカー、卸売業者、EC業者などの区分は問わない。
→「飲食店」「食品メーカー」「農業」「卸会社」「物流会社」のリストに配布予定。

■ターゲットが保有するニーズ、あるいは課題
・品質管理のために高い冷凍機能が無いといけない。
・作業品質が悪く、納期遅延や破損・汚損が発生する。
・作業に忙殺されてしまっている。
・業績拡大に合わせて倉庫を拡張したい

■訴求するベネフィット:
①最新設備があって冷凍機能〇、その他の機能も〇。
②素晴らしい設備があるので、作業品質は万全。リソースも十分。
③埼玉県の好立地に広大な倉庫があります。首都圏にもスムーズに配送
④1個、1パレット、1日の小規模案件も喜んでご対応
⑤特定の期間のみ発送を強化してほしいなど柔軟に対応します。
→「衝撃のプライス!」のように価格を強く訴求することも可
→入庫料は無料

■その他、参考表現:
・埼玉県加須市に冷凍倉庫が出来ました
・保管商品を大募集しています
・1日からでも使えます
・費用は格安、保管費用は1パレット1日40円~(税込44円)から
(※パレットとは縦110cm×横110cmの保管単位です)
・ピッキングや発送業務も承ります

■必須の項目:
・相手の社名、担当者名、電話番号、メールアドレスを書く欄
・問い合わせ先として「受付センターの電話番号とFAX番号」を記載
TEL:0120-731-904/FAX:0280-47-9163
グリーンウェーブ受付センター 埼玉県加須市松葉912
受付時間9:00~18:00(日・3が日除く)

幅広く複数案の採用を考えています。
参考資料として、これまでのFAXDMデザインをお送り致します。

以上です。
■ 選んだ理由

弊社の雰囲気に合ったデザインを選ばせていただきました。FAXDM用ですので小さい字ではなく大きな字でわかりやすいデザインが良かったです。

■ 提案者全員のお礼・コメント

ありがとうございました。次回の制作予定ががありましたら積極的に本サイトを利用させていただきます。

```html
<!DOCTYPE html>
<html lang="ja">
<head>
<meta charset="UTF-8">
<title>冷凍食品専門の物流倉庫 FAX申込書</title>
<link href="https://fonts.googleapis.com/css2?family=Noto+Sans+JP:wght@400;500;700;900&display=swap" rel="stylesheet">
<style>
  :root {
    --ink: #111;
    --paper: #fff;
    --mid: #8a8a8a;
    --light: #d9d9d9;
    --pale: #efefef;
  }
  * { box-sizing: border-box; margin: 0; padding: 0; }
  html, body { width: 849px; height: 1200px; overflow: hidden; background: var(--paper); }
  body { font-family: "Noto Sans JP", sans-serif; color: var(--ink); }
  .sheet { position: relative; width: 849px; height: 1200px; border: 2px solid var(--ink); overflow: hidden; }
  .abs { position: absolute; white-space: nowrap; }

  .tagline { left: 122px; top: 26px; width: 480px; height: 52px; background: var(--ink); color: var(--paper);
    font-weight: 900; font-size: 24px; line-height: 52px; text-align: center; }
  .headline { left: 160px; top: 90px; width: 660px; text-align: center; font-weight: 900; font-size: 42px; line-height: 58px; }
  .head-rule { left: 40px; top: 218px; width: 769px; height: 3px; background: var(--ink); }

  .benefits { left: 60px; top: 236px; width: 740px; list-style: none; font-weight: 700; font-size: 22px; line-height: 50px; }
  .benefits li::before { content: "★"; margin-right: 2px; }
  .section-rule { left: 40px; top: 512px; width: 769px; height: 2px; background: var(--ink); }

  .impact { left: 52px; top: 524px; width: 168px; height: 114px; }
  .impact-text { left: 52px; top: 540px; width: 168px; text-align: center; color: var(--paper); font-weight: 900; font-size: 32px; line-height: 40px; }
  .pill { top: 532px; height: 50px; background: var(--ink); color: var(--paper); font-weight: 900; font-size: 29px; line-height: 50px; text-align: center; }
  .pill-free { left: 296px; width: 246px; }
  .pill-day { left: 560px; width: 186px; }
  .fee-label { left: 52px; top: 640px; width: 168px; height: 128px; background: var(--ink); color: var(--paper);
    font-weight: 900; font-size: 28px; line-height: 38px; text-align: center; padding-top: 7px; }
  .price { left: 232px; top: 585px; font-weight: 900; font-size: 178px; line-height: 190px; letter-spacing: -4px; }
  .price-unit { left: 430px; top: 655px; font-weight: 900; font-size: 50px; }
  .price-tax { left: 430px; top: 722px; font-weight: 700; font-size: 24px; }
  .staff-art { left: 600px; top: 596px; width: 208px; height: 186px; border-radius: 100px 100px 10px 10px;
    background: linear-gradient(180deg, var(--pale), var(--light)); }

  .apply-band { left: 52px; top: 786px; width: 548px; height: 50px; background: var(--mid); color: var(--paper);
    font-weight: 900; font-size: 29px; line-height: 50px; padding-left: 20px; }

  .form { left: 52px; top: 842px; width: 745px; height: 250px; border: 2px solid var(--ink); }
  .form-note { position: absolute; left: 12px; top: 10px; font-size: 13px; font-weight: 500; line-height: 18px; color: #444; }
  .fax-big { position: absolute; left: 330px; top: 6px; white-space: nowrap; font-weight: 900; font-size: 40px; line-height: 54px; }
  .row { position: absolute; left: 0; width: 100%; border-top: 1.5px solid var(--ink); }
  .row-label { position: absolute; left: 12px; font-weight: 700; font-size: 19px; }
  .row-sub { position: absolute; left: 12px; font-size: 10px; color: #555; }
  .row-name { top: 66px; height: 62px; }
  .row-addr { top: 128px; height: 66px; }
  .row-tel { top: 194px; height: 54px; }
  .vline { position: absolute; background: var(--ink); width: 1.5px; }

  .footer { left: 40px; top: 1100px; width: 769px; height: 88px; background: var(--pale); }
  .center-name { left: 56px; top: 1108px; font-weight: 900; font-size: 24px; }
  .center-addr { left: 56px; top: 1148px; font-weight: 500; font-size: 17px; }
  .call-note { left: 430px; top: 1116px; width: 74px; font-size: 11px; line-height: 15px; font-weight: 500; white-space: normal; }
  .tel-icon { left: 506px; top: 1112px; }
  .tel-num { left: 550px; top: 1104px; font-weight: 900; font-size: 33px; }
  .hours { left: 550px; top: 1156px; font-size: 14px; font-weight: 500; }
</style>
</head>
<body>
<div class="sheet">
  <div class="abs tagline">「冷凍食品・冷蔵食材」の保管や発送に</div>
  <h1 class="abs headline">冷凍食品専門の物流倉庫!<br>機能充実した最新設備が特長です</h1>
  <div class="abs head-rule"></div>

  <ul class="abs benefits">
    <li>最新設備があって冷凍機能◎、その他の機能も◎!</li>
    <li>素晴らしい設備があるので、作業品質は万全。リソースも十分!</li>
    <li>埼玉県の好立地にある広大な倉庫です。首都圏にもスムーズに配送!</li>
    <li>1個、1パレット、1日の小規模案件も喜んでご対応!</li>
    <li>特定の期間のみ発送を強化してほしいなど柔軟に対応します!</li>
  </ul>
  <div class="abs section-rule"></div>

  <svg class="abs impact" viewBox="0 0 168 114" aria-hidden="true">
    <path d="M6 20 L26 4 L84 10 L142 2 L164 22 L160 60 L166 100 L130 112 L84 106 L34 112 L4 98 L10 58 Z" fill="#111"/>
  </svg>
  <div class="abs impact-text">衝撃の<br>プライス!</div>
  <div class="abs pill pill-free">入庫料は無料</div>
  <div class="abs pill pill-day">1日からOK</div>
  <div class="abs fee-label">保管費用<br>1パレット<br>1日</div>
  <div class="abs price">40</div>
  <div class="abs price-unit">円~</div>
  <div class="abs price-tax">(税込44円~)</div>
  <div class="abs staff-art" role="img" aria-label="倉庫スタッフが案内するイラスト"></div>

  <div class="abs apply-band">お申込みはこちらから!</div>

  <div class="abs form">
    <p class="form-note">下記必要事項をご記入の上<br>返信ください。</p>
    <div class="fax-big">FAX. 0280-47-9163</div>
    <div class="row row-name">
      <span class="row-sub" style="top:3px">フリガナ</span>
      <span class="row-label" style="top:22px">貴 社 名</span>
    </div>
    <div class="row row-addr">
      <span class="row-label" style="top:18px">ご住所</span>
    </div>
    <div class="row row-tel">
      <span class="row-label" style="top:12px">TEL</span>
      <span class="row-label" style="top:12px; left:390px">FAX</span>
      <div class="vline" style="left:375px; top:0; height:54px"></div>
    </div>
  </div>

  <div class="abs footer"></div>
  <div class="abs center-name">グリーンウェーブ 受付センター</div>
  <div class="abs center-addr">埼玉県加須市松葉912</div>
  <div class="abs call-note">お電話での<br>お問い合わせ</div>
  <svg class="abs tel-icon" width="38" height="38" viewBox="0 0 24 24" aria-hidden="true">
    <circle cx="12" cy="12" r="12" fill="#111"/>
    <path d="M8.2 5.5l2 2.6-1.2 1.5c.8 1.8 2.2 3.2 4 4l1.5-1.2 2.6 2-.9 2.2c-4.9-.2-8.9-4.2-9.1-9.1z" fill="#fff"/>
  </svg>
  <div class="abs tel-num">0120-731-904</div>
  <div class="abs hours">受付時間 / 9:00~18:00(日・3が日除く)</div>
</div>
</body>
</html>
```